Kiosk Coin Venture: Safe and Secure Cash Money

Front of card: LOGO

Back of card:
$$$ FREE ATM PLACEMENT $$$
BENIFITS OF HAVING AN ATM AT YOUR BUSINESS
FREE ATM and BTM (Crypto) installation, maintenance, and loading.
Lower card processing fees
Stimulate more traffic.
Ease of access for customers
Maintain customers inside location.
Higher tips and spending

Contact me for more information!
Name: Tomas Redilla
Phone: (555) 318-7742 - Call or Text
Email: Tomas@VaultLinkpay.example

Contact Information for Business Card

The card should be shape of the logo. Only the back will have all the contact and business details.

Requirements
Must have
• The logo itself will be one side, the card will be the shape of the logo. contact details on back side.

```html
<!DOCTYPE html>
<html lang="en">
<head>
<meta charset="utf-8">
<title>Kiosk Coin Venture – Business Card</title>
<link href="https://fonts.googleapis.com/css2?family=Montserrat:wght@400;500;700&display=swap" rel="stylesheet">
<style>
  :root {
    --backdrop: #ececec;
    --card-black: #000000;
    --paper-white: #ffffff;
    --silver: #d9d9d9;
    --text-white: #ffffff;
  }
  html, body {
    margin: 0;
    padding: 0;
    width: 1200px;
    height: 1200px;
    overflow: hidden;
    background: var(--backdrop);
    font-family: "Montserrat", Arial, sans-serif;
  }
  .canvas {
    position: relative;
    width: 1200px;
    height: 1200px;
  }
  .card {
    position: absolute;
    top: 180px;
    width: 493px;
    height: 841px;
    background: var(--card-black);
    color: var(--text-white);
    overflow: hidden;
    box-shadow: 0 2px 8px rgba(0,0,0,0.18);
  }
  .card-front { left: 91px; }
  .card-back  { left: 619px; }

  /* Front */
  .brand-mark {
    position: absolute;
    top: 120px;
    left: 0;
    width: 100%;
    text-align: center;
    color: var(--silver);
    font-weight: 700;
    font-size: 62px;
    line-height: 1.08;
    letter-spacing: 2px;
    text-transform: uppercase;
  }
  .brand-mark .brand-dot {
    display: block;
    width: 46px;
    height: 46px;
    margin: 0 auto 22px;
    border-radius: 50%;
    background: var(--silver);
  }
  .holder-name {
    position: absolute;
    top: 597px;
    width: 100%;
    margin: 0;
    text-align: center;
    font-weight: 700;
    font-size: 36px;
    line-height: 44px;
    letter-spacing: 1px;
  }
  .contact-icons {
    position: absolute;
    top: 654px;
    width: 100%;
    display: flex;
    justify-content: center;
    align-items: center;
    gap: 26px;
  }
  .contact-lines {
    position: absolute;
    top: 713px;
    width: 100%;
    text-align: center;
    font-size: 25px;
    line-height: 31px;
    font-weight: 400;
  }

  /* Back */
  .back-tab {
    position: absolute;
    top: 0;
    left: 0;
    width: 493px;
    height: 841px;
  }
  .back-brand {
    position: absolute;
    top: 152px;
    left: 0;
    width: 312px;
    text-align: center;
    color: var(--card-black);
    font-weight: 700;
    font-size: 40px;
    line-height: 1.1;
    letter-spacing: 1px;
    text-transform: uppercase;
  }
  .back-copy {
    position: absolute;
    top: 476px;
    left: 52px;
    width: 350px;
    font-size: 18px;
    line-height: 23px;
    font-weight: 400;
  }
  .back-copy p { margin: 0 0 23px; }
  .back-copy .benefits-title { font-weight: 700; margin: 0; }
  .back-copy ul { list-style: none; margin: 0; padding: 0; }
</style>
</head>
<body>
<main class="canvas">

  <section class="card card-front" aria-label="Card front">
    <div class="brand-mark">
      <span class="brand-dot"></span>
      Kiosk<br>Coin<br>Venture
    </div>
    <h1 class="holder-name">TOMAS REDILLA</h1>
    <div class="contact-icons">
      <svg width="28" height="28" viewBox="0 0 24 24" aria-label="Phone">
        <path d="M6.6 10.8a15 15 0 0 0 6.6 6.6l2.2-2.2a1 1 0 0 1 1-.25 11.4 11.4 0 0 0 3.6.57 1 1 0 0 1 1 1V20a1 1 0 0 1-1 1A17 17 0 0 1 3 4a1 1 0 0 1 1-1h3.5a1 1 0 0 1 1 1c0 1.25.2 2.45.57 3.57a1 1 0 0 1-.25 1z" fill="none" stroke="#fff" stroke-width="1.6"/>
        <path d="M14 3a7 7 0 0 1 7 7M14 6.5a3.5 3.5 0 0 1 3.5 3.5" fill="none" stroke="#fff" stroke-width="1.6"/>
      </svg>
      <svg width="32" height="24" viewBox="0 0 32 24" aria-label="Email">
        <rect x="1" y="1" width="30" height="22" fill="#fff"/>
        <path d="M1 1l15 12L31 1M1 23l11-10M31 23L20 13" fill="none" stroke="#000" stroke-width="1.6"/>
      </svg>
    </div>
    <div class="contact-lines">
      <div class="phone">(555) 318-7742</div>
      <div class="email">Tomas@VaultLinkpay.example</div>
    </div>
  </section>

  <section class="card card-back" aria-label="Card back">
    <svg class="back-tab" viewBox="0 0 394 674" preserveAspectRatio="none" aria-hidden="true">
      <path d="M0 0 H262 Q282 0 282 22 V238 Q282 292 125 357 Q40 322 0 296 Z" fill="#ffffff"/>
    </svg>
    <div class="back-brand">Kiosk<br>Coin<br>Venture</div>
    <div class="back-copy">
      <p>$$$ FREE ATM PLACEMENT $$$</p>
      <p class="benefits-title">BENIFITS OF HAVING AN ATM AT YOUR BUSINESS</p>
      <p>FREE ATM and BTM (Crypto) installation, maintenance, and loading.</p>
      <ul>
        <li>Lower card processing fees</li>
        <li>Stimulate more traffic.</li>
        <li>Ease of access for customers</li>
        <li>Maintain customers inside location.</li>
        <li>Higher tips and spending</li>
      </ul>
    </div>
  </section>

</main>
</body>
</html>
```